Kovalen Spinal Care and Performance

We need new business cards, something more modern, clean. On the back of the card maybe a quote. The Dr. likes, “The doctor of the future will give no medicine, but will interest his patient in the care of the human frame, in diet and in the cause and prevention of disease.” - Walter Brisby. We are open to other suggestions. We are a chiropractic office.

```html
<!DOCTYPE html>
<html lang="en">
<head>
<meta charset="utf-8">
<title>Kovalen Spinal Care and Performance – Business Cards</title>
<link href="https://fonts.googleapis.com/css2?family=Libre+Baskerville:wght@700&family=Roboto:wght@400;500&display=swap" rel="stylesheet">
<style>
  :root {
    --purple: #5f2a6e;
    --purple-dark: #4e1f5c;
    --green: #8db236;
    --white: #ffffff;
    --stage: #2b2b2b;
    --text-font: "Roboto", Arial, sans-serif;
    --name-font: "Libre Baskerville", Georgia, serif;
  }
  * { box-sizing: border-box; margin: 0; padding: 0; }
  html, body { width: 1200px; height: 900px; overflow: hidden; }
  body { background: var(--stage); position: relative; font-family: var(--text-font); }

  .card {
    position: absolute;
    width: 540px;
    height: 310px;
    border-radius: 14px;
    overflow: hidden;
    background: var(--white);
    box-shadow: 0 14px 30px rgba(0,0,0,.45);
  }

  /* Quote side */
  .card--quote { left: 50px; top: 130px; }
  .quote-brand {
    position: absolute; left: 0; right: 0; top: 78px;
    text-align: center;
  }
  .brand-name {
    font-family: var(--text-font);
    font-weight: 500;
    color: var(--purple);
    letter-spacing: .02em;
  }
  .quote-brand .brand-name { font-size: 25px; line-height: 1.25; }
  .quote-brand .brand-dot {
    display: inline-block; width: 12px; height: 12px; border-radius: 50%;
    background: var(--green); margin-bottom: 10px;
  }
  .quote-band {
    position: absolute; left: 0; right: 0; bottom: 0; height: 92px;
    background: var(--purple);
    padding: 16px 26px 0;
    color: var(--white);
  }
  .quote-text { font-size: 13.5px; line-height: 1.4; }
  .quote-author {
    position: absolute; right: 22px; bottom: 10px;
    font-size: 9px; color: var(--green);
  }

  /* Contact side */
  .card--contact { left: 610px; top: 450px; background: var(--purple); }
  .contact-curve { position: absolute; inset: 0; }
  .contact-brand {
    position: absolute; right: 22px; top: 72px; width: 190px;
    text-align: center;
  }
  .contact-brand .brand-name { font-size: 17px; line-height: 1.25; }
  .contact-brand .brand-dot {
    display: inline-block; width: 9px; height: 9px; border-radius: 50%;
    background: var(--green); margin-bottom: 6px;
  }
  .person { position: absolute; left: 34px; top: 56px; color: var(--white); }
  .person-name { font-family: var(--name-font); font-size: 23px; }
  .person-role { font-size: 13px; font-weight: 500; margin: 6px 0 0 18px; }
  .address {
    position: absolute; left: 52px; top: 150px;
    color: var(--white); font-size: 13.5px; font-weight: 500; line-height: 1.35;
  }
  .contact-list {
    position: absolute; left: 34px; top: 218px; list-style: none;
    color: var(--white); font-size: 13px; font-weight: 500;
  }
  .contact-list li { display: flex; align-items: center; height: 24px; }
  .contact-icon {
    width: 15px; height: 15px; margin-right: 12px;
    background: var(--green); display: inline-flex;
    align-items: center; justify-content: center;
  }
</style>
</head>
<body>

<section class="card card--quote" aria-label="Card front with quote">
  <div class="quote-brand">
    <span class="brand-dot"></span>
    <p class="brand-name">Kovalen<br>Spinal Care and Performance</p>
  </div>
  <div class="quote-band">
    <p class="quote-text">“The doctor of the future will give no medicine, but will interest his patient in the care of the human frame, in diet and in the cause and prevention of disease.”</p>
    <span class="quote-author">- Walter Brisby</span>
  </div>
</section>

<section class="card card--contact" aria-label="Card back with contact details">
  <svg class="contact-curve" width="540" height="310" viewBox="0 0 540 310">
    <path d="M262 0 Q268 215 540 282 L540 0 Z" fill="#ffffff"/>
    <path d="M290 0 Q298 200 540 262 L540 0 Z" fill="#5f2a6e"/>
    <path d="M300 0 Q306 196 540 256 L540 0 Z" fill="#8db236"/>
    <path d="M310 0 Q316 186 540 246 L540 0 Z" fill="#ffffff"/>
  </svg>

  <div class="contact-brand">
    <span class="brand-dot"></span>
    <p class="brand-name">Kovalen<br>Spinal Care and Performance</p>
  </div>

  <div class="person">
    <p class="person-name">Marin Ashcroft</p>
    <p class="person-role">Doctor</p>
  </div>

  <p class="address">Suite 4, 18 Corlow Street<br>TALLOWOOD NSW 2099</p>

  <ul class="contact-list">
    <li>
      <span class="contact-icon">
        <svg width="9" height="9" viewBox="0 0 10 10"><path d="M2 1 L4 1 L4.6 3.2 L3.4 4 Q4.4 5.8 6 6.6 L6.8 5.4 L9 6 L9 8 Q9 9 8 9 Q1 8.5 1 2 Q1 1 2 1 Z" fill="#fff"/></svg>
      </span>(02) 9000 4187
    </li>
    <li>
      <span class="contact-icon">
        <svg width="9" height="9" viewBox="0 0 10 10"><rect x="1" y="2.5" width="8" height="5.5" fill="none" stroke="#fff" stroke-width="1"/><path d="M1 2.5 L5 5.5 L9 2.5" fill="none" stroke="#fff" stroke-width="1"/></svg>
      </span>marin.ashcroft@kovalenspinal.com.au
    </li>
    <li>
      <span class="contact-icon">
        <svg width="9" height="9" viewBox="0 0 10 10"><circle cx="5" cy="5" r="3.8" fill="none" stroke="#fff" stroke-width="1"/><ellipse cx="5" cy="5" rx="1.6" ry="3.8" fill="none" stroke="#fff" stroke-width=".8"/><line x1="1.2" y1="5" x2="8.8" y2="5" stroke="#fff" stroke-width=".8"/></svg>
      </span>www.kovalenspinal.com.au
    </li>
  </ul>
</section>

</body>
</html>
```